I need 2 flyers designed for my business

Both can be similar in design and will have different purposes. I need an education based flyer and I need a government based flyer. The focus of the flyer will be software on the front and services on the back.
These all need to be 8.5x 11 in dimension (they can be full bleed). I would like to be able to print these out if needed. The design needs to look good with our website > www.brintalo.com

The software details are on the website.

```html
<!DOCTYPE html>
<html lang="en">
<head>
<meta charset="UTF-8">
<title>Our Services</title>
<link rel="stylesheet" href="https://fonts.googleapis.com/css2?family=Montserrat:wght@300;400&family=Poppins:wght@700;800&display=swap">
<style>
  :root {
    --crimson: #860000;
    --crimson-deep: #5a0c0c;
    --olive-light: #958224;
    --olive-dark: #6e5800;
    --gold: #9a8a26;
    --white: #ffffff;
    --rule: rgba(255, 255, 255, 0.55);
  }
  * { margin: 0; padding: 0; box-sizing: border-box; }
  html, body { width: 927px; height: 1200px; overflow: hidden; }
  body { position: relative; background: var(--crimson-deep); color: var(--white); }

  .backdrop {
    position: absolute; inset: 0;
    background:
      radial-gradient(ellipse at 60% 10%, #9a1a14 0%, transparent 55%),
      radial-gradient(ellipse at 20% 75%, #6e0e0e 0%, transparent 60%),
      linear-gradient(160deg, #7a1010 0%, #4a0a0a 50%, #6a0c0c 100%);
  }

  .heading { position: absolute; left: 0; width: 927px; text-align: center; }
  .heading-our {
    top: 30px;
    font-family: 'Montserrat', sans-serif; font-weight: 300;
    font-size: 82px; line-height: 1; color: var(--gold); letter-spacing: -1px;
  }
  .heading-services {
    top: 100px;
    font-family: 'Poppins', sans-serif; font-weight: 800;
    font-size: 102px; line-height: 1; letter-spacing: 2px;
    background: linear-gradient(180deg, #ffffff 30%, #c9c4c4 100%);
    -webkit-background-clip: text; background-clip: text; color: transparent;
  }

  .band { position: absolute; left: 0; width: 927px; }
  .band-scanning { top: 186px; height: 279px; background: var(--crimson); border-radius: 0 140px 140px 0; }
  .band-storage { top: 499px; height: 307px; background: linear-gradient(90deg, var(--olive-light), var(--olive-dark)); border-radius: 154px 0 0 154px; }
  .band-shredding { top: 840px; height: 308px; background: var(--crimson); border-radius: 0 154px 154px 0; }

  .column-rule { position: absolute; top: 186px; height: 962px; width: 1px; background: var(--rule); }
  .column-rule.first { left: 223px; }
  .column-rule.second { left: 534px; }

  .service-icon {
    position: absolute; left: 86px; width: 74px; height: 74px; border-radius: 50%;
    display: flex; align-items: center; justify-content: center;
  }
  .service-icon.gold { background: var(--gold); }
  .service-icon.red { background: #a52a1e; }

  .service-title {
    position: absolute; left: 20px; width: 206px; text-align: center;
    font-family: 'Poppins', sans-serif; font-weight: 700;
    font-size: 20.5px; line-height: 24px; letter-spacing: 0.4px; text-transform: uppercase;
  }

  .service-summary {
    position: absolute; left: 254px; width: 272px;
    font-family: 'Poppins', sans-serif; font-weight: 700;
    font-size: 15.6px; line-height: 24.3px;
  }

  .service-points { position: absolute; left: 567px; width: 340px; }
  .points-heading {
    font-family: 'Poppins', sans-serif; font-weight: 700;
    font-size: 16.6px; line-height: 24px; margin-bottom: 3px;
  }
  .points-list { list-style: none; font-family: 'Montserrat', sans-serif; font-weight: 400; font-size: 15.6px; line-height: 27.3px; }
  .points-list svg { display: inline-block; width: 12px; height: 12px; margin-right: 6px; vertical-align: -1px; }
</style>
</head>
<body>
  <div class="backdrop" role="img" aria-label="Blurred red-toned photo of an office desk with paperwork"></div>

  <h1>
    <span class="heading heading-our">OUR</span>
    <span class="heading heading-services">SERVICES</span>
  </h1>

  <div class="band band-scanning"></div>
  <div class="band band-storage"></div>
  <div class="band band-shredding"></div>

  <div class="column-rule first"></div>
  <div class="column-rule second"></div>

  <!-- Scanning -->
  <div class="service-icon gold" style="top:242px;">
    <svg width="36" height="40" viewBox="0 0 36 40" fill="none" stroke="#fff" stroke-width="1.4">
      <rect x="4" y="8" width="22" height="28" rx="1"/>
      <rect x="7" y="5" width="22" height="28" rx="1"/>
      <path d="M10 2h16l6 6v26H10z"/>
      <path d="M26 2v6h6"/>
      <path d="M14 14h14M14 18h14M14 22h14M14 26h10"/>
    </svg>
  </div>
  <h2 class="service-title" style="top:320px;">Document<br>Scanning<br>Services</h2>
  <p class="service-summary" style="top:264px;">Fast, efficient process for the conversion of existing paper records to digital archives, increasing access and reducing onsite storage and costs.</p>
  <div class="service-points" style="top:258px;">
    <h3 class="points-heading">Scanning services for any format:</h3>
    <ul class="points-list">
      <li><svg viewBox="0 0 12 12"><path d="M0 1h5l7 5-7 5H0l6-5z" fill="#a8902a"/></svg>Standard Office Documents</li>
      <li><svg viewBox="0 0 12 12"><path d="M0 1h5l7 5-7 5H0l6-5z" fill="#a8902a"/></svg>16mm, 35mm Roll Microfilm</li>
      <li><svg viewBox="0 0 12 12"><path d="M0 1h5l7 5-7 5H0l6-5z" fill="#a8902a"/></svg>Microfiche (Jackets or COM)</li>
      <li><svg viewBox="0 0 12 12"><path d="M0 1h5l7 5-7 5H0l6-5z" fill="#a8902a"/></svg>Large Format Documents/ Drawings</li>
    </ul>
  </div>

  <!-- Storage -->
  <div class="service-icon red" style="top:574px;">
    <svg width="36" height="40" viewBox="0 0 36 40" fill="none" stroke="#fff" stroke-width="1.4">
      <ellipse cx="18" cy="7" rx="15" ry="5"/>
      <path d="M3 7v26c0 3 7 5 15 5s15-2 15-5V7"/>
      <path d="M3 16c0 3 7 5 15 5s15-2 15-5M3 25c0 3 7 5 15 5s15-2 15-5"/>
      <path d="M24 13h1M27 12h1M24 22h1M27 21h1M24 31h1M27 30h1" stroke-linecap="round"/>
    </svg>
  </div>
  <h2 class="service-title" style="top:653px;">Document<br>Storage<br>Services</h2>
  <p class="service-summary" style="top:593px;">Solution for offsite document storage and retrieval to effectively store, manage, and safeguard your vital business records and documents.</p>
  <div class="service-points" style="top:589px;">
    <h3 class="points-heading">A local, convenient solution:</h3>
    <ul class="points-list">
      <li><svg viewBox="0 0 12 12"><path d="M0 1h5l7 5-7 5H0l6-5z" fill="#a01a10"/></svg>Free Up Office Space</li>
      <li><svg viewBox="0 0 12 12"><path d="M0 1h5l7 5-7 5H0l6-5z" fill="#a01a10"/></svg>Reduce Costs</li>
      <li><svg viewBox="0 0 12 12"><path d="M0 1h5l7 5-7 5H0l6-5z" fill="#a01a10"/></svg>Keep Records in a Fireproof,</li>
      <li><svg viewBox="0 0 12 12"><path d="M0 1h5l7 5-7 5H0l6-5z" fill="#a01a10"/></svg>Waterproof &amp; Wind-Safe Facility</li>
    </ul>
  </div>

  <!-- Shredding -->
  <div class="service-icon gold" style="top:913px;">
    <svg width="38" height="38" viewBox="0 0 38 38" fill="none" stroke="#fff" stroke-width="1.4">
      <path d="M10 12V3h15l4 4v5"/>
      <rect x="3" y="12" width="32" height="11" rx="2"/>
      <circle cx="8" cy="19" r="1"/><circle cx="12" cy="19" r="1"/>
      <path d="M8 23h22"/>
      <path d="M10 23v10M14 23v12M18 23v9M22 23v11M26 23v10"/>
    </svg>
  </div>
  <h2 class="service-title" style="top:991px;">Secure<br>Document<br>Shredding</h2>
  <p class="service-summary" style="top:933px;">Safely and cost-effectively destroy unnecessary paper- based documents. One-time or recurring, our solutions are tailored to you.</p>
  <div class="service-points" style="top:927px;">
    <h3 class="points-heading">Destroy Unnecessary Documents:</h3>
    <ul class="points-list">
      <li><svg viewBox="0 0 12 12"><path d="M0 1h5l7 5-7 5H0l6-5z" fill="#a8902a"/></svg>Protect confidential information</li>
      <li><svg viewBox="0 0 12 12"><path d="M0 1h5l7 5-7 5H0l6-5z" fill="#a8902a"/></svg>Reduce the cost of managing information that is no longer useful</li>
      <li><svg viewBox="0 0 12 12"><path d="M0 1h5l7 5-7 5H0l6-5z" fill="#a8902a"/></svg>Ensure compliance with regulations for information destruction</li>
    </ul>
  </div>
</body>
</html>
```